Simple Clean Menu for 'Toasty Biscuits & Batter'!!!!

We are needing a menu for a cookie & cookie dough shop in the Philadelphia PA area called 'Toasty' We make delicious edible cookie doughs and warm cookies.

Attached to the project is the following
1.  The menu content and pricing
2.  A competitors menu (we want it to look better than theirs!)
3.  Our logo
4. Some Images of what we serve so you better understand.
5. A hand drawn sketch we made (keep in mind we do not want a vertical menu... its just to help get your mind going)

We want the menu to be horizontal and the sections should be divided in columns from left to right not top to bottom. Column 1 - cookie dough section(with toppings at the bottom), Column 2 (or 2+3)- Gourmet cookie and signature cookie column, Column 3 (or 4) -bakedwiches and drinks

We would like custom icon designs for the dough with 1,2,3 scoops - (refer to drawings) for the cookies (not necessarily every flavor), and definitely for the bakedwiches.

The dimensions of our in store sign will be 29.75 inches h x 69.5 inches w horizontal and it will be hanging on the wall and we need all source files and infinitely scalable photoshop pdf and of course follow a lighter color scheme according to our logo etc.

Industry/Entity Type

Shop

Font styles to use
Sans Serif
Other font styles liked:
• Refer to Description + Documents

Requirements
Must have
Nice to have
Should not have

```html
<!DOCTYPE html>
<html lang="en">
<head>
<meta charset="utf-8">
<title>Toasty Biscuits &amp; Batter Menu</title>
<link href="https://fonts.googleapis.com/css2?family=Fredoka:wght@400;500;600&family=Josefin+Sans:wght@400;600&display=swap" rel="stylesheet">
<style>
  :root {
    --pink: #f01ec8;
    --pink-soft: #fbd3f2;
    --orange: #f3a633;
    --orange-soft: #fde3b6;
    --cyan: #8fe3e8;
    --cyan-pale: #e3f8f9;
    --ink: #2e2e2e;
    --text: #3a3a3a;
    --paper: #ffffff;
  }
  * { margin: 0; padding: 0; box-sizing: border-box; }
  html, body { width: 1200px; height: 514px; overflow: hidden; background: var(--paper); }
  .menu { position: relative; width: 1200px; height: 514px; font-family: "Josefin Sans", sans-serif; color: var(--text); }

  .band { position: absolute; top: 44px; height: 36px; background: var(--cyan-pale); border-top: 1px solid var(--cyan); border-bottom: 1px solid var(--cyan); }
  .band--left { left: 0; width: 460px; }
  .band--right { right: 0; width: 460px; }
  .brand { position: absolute; left: 460px; top: 34px; width: 280px; height: 56px; display: flex; align-items: center; justify-content: center; gap: 10px; }
  .brand__dot { width: 40px; height: 40px; border-radius: 50%; background: var(--orange); flex: none; }
  .brand__name { font-family: "Fredoka", sans-serif; font-weight: 600; font-size: 20px; color: var(--ink); white-space: nowrap; }

  .divider { position: absolute; top: 116px; width: 1px; height: 368px; background: var(--cyan); }

  .heading { position: absolute; width: 204px; height: 42px; border: 2px solid var(--pink); border-radius: 4px; display: flex; align-items: center; justify-content: center; font-family: "Fredoka", sans-serif; font-weight: 500; font-size: 21px; color: var(--orange); letter-spacing: .5px; }

  .blurb { position: absolute; font-size: 7.4px; line-height: 1.35; text-align: justify; }

  .art { position: absolute; border-radius: 6px; }
  .art--warm { background: linear-gradient(90deg, var(--pink-soft), var(--orange-soft)); }
  .art--orange { background: var(--orange-soft); }
  .art--pink { background: var(--pink-soft); }

  .cup-prices { position: absolute; left: 46px; top: 252px; width: 210px; height: 14px; font-family: "Fredoka", sans-serif; font-weight: 600; font-size: 8.5px; color: var(--ink); }
  .cup-prices span { position: absolute; width: 40px; text-align: center; }

  .note { position: absolute; left: 46px; top: 287px; width: 204px; font-size: 11px; color: var(--orange); text-align: center; }

  .toppings-text { position: absolute; left: 46px; top: 372px; width: 216px; font-size: 11.5px; line-height: 1.3; }
  .toppings-text strong { font-weight: 600; color: var(--ink); }

  .prices { position: absolute; font-family: "Fredoka", sans-serif; font-weight: 600; font-size: 12px; color: var(--ink); }
  .prices span { position: absolute; text-align: center; white-space: nowrap; }

  .flavors { position: absolute; list-style: none; text-align: center; font-family: "Fredoka", sans-serif; font-weight: 500; text-transform: uppercase; }
  .flavors li:nth-child(odd) { color: var(--orange); }
  .flavors li:nth-child(even) { color: var(--pink); }
  .flavors--signature { left: 334px; width: 224px; top: 314px; font-size: 15px; }
  .flavors--signature li { height: 35px; line-height: 22px; }
  .flavors--gourmet { left: 626px; width: 244px; top: 254px; font-size: 13.5px; }
  .flavors--gourmet li { height: 28px; line-height: 20px; }

  .wich { position: absolute; left: 914px; width: 248px; display: flex; gap: 10px; }
  .wich__icon { flex: none; width: 34px; height: 22px; border-radius: 5px; margin-top: 1px; }
  .wich__title { font-family: "Fredoka", sans-serif; font-weight: 500; font-size: 12.5px; text-transform: uppercase; line-height: 1.15; white-space: nowrap; }
  .wich__desc { font-size: 7.2px; line-height: 1.3; margin-top: 2px; text-align: justify; }
  .wich--pink .wich__title { color: var(--pink); }
  .wich--orange .wich__title { color: var(--orange); }

  .drinks { position: absolute; left: 958px; top: 430px; list-style: none; font-family: "Fredoka", sans-serif; font-weight: 500; font-size: 12.5px; line-height: 20px; }
  .drinks li:nth-child(odd) { color: var(--orange); }
  .drinks li:nth-child(even) { color: var(--pink); }
</style>
</head>
<body>
<main class="menu">
  <div class="band band--left"></div>
  <div class="band band--right"></div>
  <header class="brand">
    <span class="brand__dot"></span>
    <span class="brand__name">Toasty Biscuits &amp; Batter</span>
  </header>

  <div class="divider" style="left:298px"></div>
  <div class="divider" style="left:598px"></div>
  <div class="divider" style="left:898px"></div>

  <!-- Cookie dough -->
  <h2 class="heading" style="left:46px;top:117px">Cookie Dough</h2>
  <p class="blurb" style="left:46px;top:172px;width:208px">Try our many flavors of delicious edible cookie dough. Our dough tastes just like it should so you'll never know it's egg free and completely safe to eat! In a cone, in a cup, warm or cold there's no wrong way to eat our dough.</p>
  <div class="art art--pink" style="left:46px;top:222px;width:210px;height:50px" role="img" aria-label="Icons of dough cups with one, two and three scoops and a cone add-on"></div>
  <div class="cup-prices">
    <span style="left:0">$4</span><span style="left:56px">$7</span><span style="left:118px">$9</span><span style="left:172px">+ $1</span>
  </div>
  <p class="note">Eat it in a cone for $1!</p>

  <h2 class="heading" style="left:46px;top:321px">Toppings</h2>
  <p class="toppings-text">Add Marshmallow, Caramel, Chocolate Syrup or Whipped Cream for <strong>$0.50</strong> each!</p>
  <div class="art art--warm" style="left:46px;top:422px;width:210px;height:58px" role="img" aria-label="Topping illustrations: syrup bottle, whipped cream, caramel splash and marshmallows"></div>

  <!-- Signature cookies -->
  <h2 class="heading" style="left:344px;top:117px">Signature Cookies</h2>
  <p class="blurb" style="left:344px;top:172px;width:210px">Our most decadent, gourmet cookies. 100% GMO Free, Free from Artificial colors and flavorings and made with milk, cream and butter from happy hormone free cows!</p>
  <div class="art art--warm" style="left:340px;top:224px;width:216px;height:40px" role="img" aria-label="Cookie icons for a single cookie, a six pack and a dozen"></div>
  <div class="prices" style="left:334px;top:266px;width:220px">
    <span style="left:0;width:30px">$3</span><span style="left:78px;width:60px">$16</span><span style="left:164px;width:50px">$30</span>
  </div>
  <ul class="flavors flavors--signature">
    <li>Chocolate Chunk</li><li>Salted Caramel</li><li>Lemon Blueberry</li><li>Snickerdoodle</li><li>Peanut Butter</li>
  </ul>

  <!-- Gourmet cookies -->
  <h2 class="heading" style="left:646px;top:117px">Gourmet Cookies</h2>
  <div class="art art--warm" style="left:636px;top:176px;width:230px;height:40px" role="img" aria-label="Cookie icons for a single cookie, a six pack and a dozen"></div>
  <div class="prices" style="left:630px;top:218px;width:240px">
    <span style="left:0;width:40px">$1.50</span><span style="left:80px;width:40px">$ 8</span><span style="left:166px;width:44px">$15</span>
  </div>
  <ul class="flavors flavors--gourmet">
    <li>Chocolate Chip</li><li>Oatmeal Raisin</li><li>White Chocolate Macademia</li><li>Gluten Free Chocolate Chip</li><li>Toffee Crunch</li><li>Red Velvet</li><li>Sugar</li><li>Candy Button</li>
  </ul>

  <!-- Toastywiches -->
  <h2 class="heading" style="left:946px;top:117px">Toastywiches</h2>
  <div class="wich wich--pink" style="top:176px">
    <div class="wich__icon art--orange" role="img" aria-label="Cookie sandwich icon"></div>
    <div><h3 class="wich__title">The "Un-Toastywich" $6</h3><p class="wich__desc">Any flavor of our delicious cookie dough stuffed between your choice of two Gourmet Cookies!</p></div>
  </div>
  <div class="wich wich--orange" style="top:226px">
    <div class="wich__icon art--pink" role="img" aria-label="Ice cream sandwich icon"></div>
    <div><h3 class="wich__title">The Ice Cream Toastywich $5</h3><p class="wich__desc">Creamy vanilla ice cream stuffed between your choice of any two Gourmet Cookies!</p></div>
  </div>
  <div class="wich wich--pink" style="top:275px">
    <div class="wich__icon art--orange" role="img" aria-label="Dough sandwich icon"></div>
    <div><h3 class="wich__title">The Ice Cream Doughwich $6</h3><p class="wich__desc">Creamy vanilla ice cream stuffed between delicious chocolate chip cookie dough…nuff said</p></div>
  </div>
  <div class="wich wich--orange" style="top:326px">
    <div class="wich__icon art--pink" role="img" aria-label="Signature cookie sandwich icon"></div>
    <div><h3 class="wich__title">Signature Upgrade: $2.50</h3><p class="wich__desc">Make any Toastywich with any two Signature Cookies for just $2.50!</p></div>
  </div>

  <!-- Drinks -->
  <h2 class="heading" style="left:946px;top:378px">Drinks</h2>
  <ul class="drinks">
    <li>Water: $2.25</li><li>Organic Chocolate Milk:&nbsp; $3</li><li>Organic Milk:&nbsp; $3</li>
  </ul>
</main>
</body>
</html>
```